I need a folder to put papers in when I am scheduling patients for surgery. The information is general, such as costs, consent forms etc. The folder is designed to give the patient these papers in a neat manner. The cover of the folder needs to use my brand and perhaps create some interest when it is sitting on their kitchen bench with visitors and family. I'll attach a typical template for a folder. It needs to be stylish, classic and professional, as I am about to operate on the person's eye. <br/>I would like my logo included. I'll also attach a photo which is on my website which might work to wrap around the folder. The website address is bramwelkoske.com.au and you can see the way the image is used there on most of the pages as a banner. My profile photo could possibly used as well. Perhaps on the back, but if it looks strange then that is not necessary. The contact information need not be on the folder. Just Dr Lars Brimwell, Ophthalmic Surgeon. Finally, our brand slogan is. "The world's a beautiful place, see it clearly". This could also be on it. Again, this all needs to be professional looking. <br/>I've attached all our previous design jobs, 2 profile pictures, and the image that I think would work. Please also look at the website. <br/><br/>The second part of the project is to create a business card for my practice manager. Her name is Fiona Pelkrest<br/>It should include<br/>Fiona Pelkrest (BCom)<br/>Practice Manager for Dr Lars Brimwell<br/>Ophthalmic Surgeon <br/><br/>Then all the details which are on our current business card<br/><br/><br/><br/><br/>

Contact Information for Business Card

Just match the business cards I already have, but use the details above

Colors

Designer to choose colors to be used in the design.

```html
<!DOCTYPE html>
<html lang="en">
<head>
<meta charset="utf-8">
<title>Dr Lars Brimwell – Patient Folder and Stationery</title>
<link href="https://fonts.googleapis.com/css2?family=Open+Sans:wght@400;600;700&family=Poppins:wght@300;600&family=Roboto:wght@400;500&display=swap" rel="stylesheet">
<style>
  :root {
    --board: #2b2b2b;
    --white: #ffffff;
    --brand-blue: #2a7cc4;
    --brand-blue-deep: #1f6fb8;
    --brand-blue-light: #3d97d8;
    --text-grey: #4a4a4a;
    --silver: #b9b9b9;
    --cap-dark: #2f2f2f;
  }
  * { margin: 0; padding: 0; box-sizing: border-box; }
  html, body { width: 1189px; height: 1200px; overflow: hidden; background: var(--board); }
  body { position: relative; font-family: "Open Sans", sans-serif; }
  .panel-title {
    position: absolute; top: 60px; width: 493px; text-align: center;
    color: var(--white); font-family: "Roboto", sans-serif; font-size: 22px; font-weight: 400;
  }
  .panel-title--front { left: 79px; }
  .panel-title--back { left: 614px; }
  .folder { position: absolute; top: 100px; width: 493px; height: 657px; display: block; }
  .folder--front { left: 79px; }
  .folder--back { left: 614px; }
  .card { position: absolute; top: 863px; width: 351px; height: 200px; display: block; }
  .card--brand { left: 79px; }
  .card--manager { left: 461px; }
  .usb { position: absolute; left: 906px; width: 130px; height: 52px; display: block; }
  .usb--white { top: 881px; }
  .usb--blue { top: 991px; }
  .brand-name { font-family: "Open Sans", sans-serif; font-weight: 600; fill: var(--brand-blue); }
  .brand-role { font-family: "Open Sans", sans-serif; font-weight: 600; fill: var(--text-grey); }
  .brand-quals { font-family: "Open Sans", sans-serif; font-weight: 400; fill: var(--text-grey); }
  .slogan { font-family: "Poppins", sans-serif; fill: var(--white); }
  .web { font-family: "Roboto", sans-serif; fill: var(--white); letter-spacing: 1.6px; }
  .contact { font-family: "Roboto", sans-serif; fill: var(--text-grey); }
  .contact-light { font-family: "Roboto", sans-serif; fill: var(--white); }
</style>
</head>
<body>

<div class="panel-title panel-title--front">Folder Front Side</div>
<div class="panel-title panel-title--back">Folder Back Side</div>

<!-- Folder front -->
<svg class="folder folder--front" viewBox="0 0 493 657" xmlns="http://www.w3.org/2000/svg">
  <defs>
    <linearGradient id="bandBlue" x1="0" y1="0" x2="1" y2="0">
      <stop offset="0" stop-color="#2474bd"/>
      <stop offset="1" stop-color="#3a95d6"/>
    </linearGradient>
    <linearGradient id="silverLine" x1="0" y1="0" x2="1" y2="0">
      <stop offset="0" stop-color="#8c8c8c"/>
      <stop offset="0.5" stop-color="#e6e6e6"/>
      <stop offset="1" stop-color="#8c8c8c"/>
    </linearGradient>
    <radialGradient id="sunset" cx="0.3" cy="0.45" r="0.7">
      <stop offset="0" stop-color="#fff3b0"/>
      <stop offset="0.12" stop-color="#f5b640"/>
      <stop offset="0.4" stop-color="#b9874a"/>
      <stop offset="0.7" stop-color="#4d4a44"/>
      <stop offset="1" stop-color="#1f2226"/>
    </radialGradient>
    <clipPath id="bandClip"><rect x="0" y="236" width="493" height="279"/></clipPath>
  </defs>
  <rect width="493" height="657" fill="var(--white)"/>

  <g class="logo">
    <circle cx="120" cy="110" r="12" fill="var(--brand-blue)"/>
    <text class="brand-name" x="142" y="119" font-size="26">Dr Lars Brimwell</text>
    <text class="brand-role" x="143" y="135" font-size="10">Ophthalmic Surgeon</text>
    <text class="brand-quals" x="143" y="146" font-size="8">MBBS (Hons) MMed FRANZCO</text>
  </g>

  <rect y="231" width="493" height="5" fill="url(#silverLine)"/>
  <rect y="236" width="493" height="279" fill="url(#bandBlue)"/>
  <circle cx="585" cy="375" r="305" fill="url(#sunset)" clip-path="url(#bandClip)"
          role="img" aria-label="Photograph of the sun setting over the ocean"/>
  <text class="slogan" x="140" y="350" font-size="25" font-weight="300" text-anchor="middle">The world's a</text>
  <text class="slogan" x="140" y="384" font-size="26" font-weight="600" text-anchor="middle">Beautiful Place,</text>
  <text class="slogan" x="140" y="417" font-size="25" font-weight="300" text-anchor="middle">see it clearly</text>
  <rect y="515" width="493" height="5" fill="url(#silverLine)"/>

  <path d="M0,643 Q246,598 493,643 L493,657 L0,657 Z" fill="var(--brand-blue)"/>
  <path d="M0,641 Q246,596 493,641" fill="none" stroke="url(#silverLine)" stroke-width="3"/>
  <text class="web" x="246" y="646" font-size="11" text-anchor="middle">bramwelkoske.com.au</text>
</svg>

<!-- Folder back -->
<svg class="folder folder--back" viewBox="0 0 493 657" xmlns="http://www.w3.org/2000/svg">
  <defs>
    <radialGradient id="backBlue" cx="0.5" cy="0.4" r="0.8">
      <stop offset="0" stop-color="#3c97d8"/>
      <stop offset="1" stop-color="#2372bb"/>
    </radialGradient>
    <linearGradient id="silverArc" x1="0" y1="0" x2="1" y2="0">
      <stop offset="0" stop-color="#8c8c8c"/>
      <stop offset="0.5" stop-color="#e6e6e6"/>
      <stop offset="1" stop-color="#8c8c8c"/>
    </linearGradient>
    <linearGradient id="portraitTone" x1="0" y1="0" x2="0" y2="1">
      <stop offset="0" stop-color="#6c8fae"/>
      <stop offset="0.5" stop-color="#c9b8a2"/>
      <stop offset="1" stop-color="#b8aa98"/>
    </linearGradient>
  </defs>
  <rect width="493" height="657" fill="var(--white)"/>

  <g class="logo">
    <circle cx="172" cy="92" r="12" fill="var(--brand-blue)"/>
    <text class="brand-name" x="194" y="102" font-size="26">Dr Lars Brimwell</text>
    <text class="brand-role" x="195" y="117" font-size="10">Ophthalmic Surgeon</text>
    <text class="brand-quals" x="195" y="127" font-size="8">MBBS (Hons) MMed FRANZCO</text>
  </g>

  <path d="M0,217 Q246,180 493,217 L493,657 L0,657 Z" fill="url(#backBlue)"/>
  <path d="M0,215 Q246,178 493,215" fill="none" stroke="url(#silverArc)" stroke-width="3"/>

  <rect x="250" y="394" width="243" height="263" rx="110" ry="90" fill="url(#portraitTone)"
        role="img" aria-label="Portrait photograph of Dr Lars Brimwell"/>

  <g class="back-contact">
    <text class="contact-light" x="23" y="551" font-size="13" font-weight="500">Dr Lars Brimwell</text>
    <text class="contact-light" x="23" y="560" font-size="4.5">Ophthalmic Surgeon</text>
    <text class="contact-light" x="23" y="566" font-size="4.5">MBBS (Hons) MMed FRANZCO</text>
    <circle cx="26" cy="581" r="2.2" fill="var(--white)"/>
    <text class="contact-light" x="31" y="583" font-size="5.6">(08) 9471 2630</text>
    <circle cx="26" cy="588.5" r="2.2" fill="var(--white)"/>
    <text class="contact-light" x="31" y="590.5" font-size="5.6">(08) 9471 2638</text>
    <circle cx="26" cy="596" r="2.2" fill="var(--white)"/>
    <text class="contact-light" x="31" y="598" font-size="5.6">reception@bramwelkoske.com.au</text>
    <text class="contact-light" x="23" y="612" font-size="5.6">24 Harrow Lane, Westmere</text>
    <text class="contact-light" x="23" y="619" font-size="5.6">Western Australia 6015</text>
    <text class="contact-light" x="23" y="633" font-size="5.6">bramwelkoske.com.au</text>
  </g>
</svg>

<!-- Brand business card -->
<svg class="card card--brand" viewBox="0 0 351 200" xmlns="http://www.w3.org/2000/svg">
  <defs>
    <clipPath id="cardClipA"><rect width="351" height="200" rx="8"/></clipPath>
    <linearGradient id="silverCardA" x1="0" y1="0" x2="1" y2="0">
      <stop offset="0" stop-color="#8c8c8c"/>
      <stop offset="0.5" stop-color="#e6e6e6"/>
      <stop offset="1" stop-color="#8c8c8c"/>
    </linearGradient>
  </defs>
  <g clip-path="url(#cardClipA)">
    <rect width="351" height="200" fill="var(--white)"/>
    <circle cx="118" cy="84" r="11" fill="var(--brand-blue)"/>
    <text class="brand-name" x="137" y="92" font-size="24">Dr Lars Brimwell</text>
    <text class="brand-role" x="138" y="108" font-size="9">Ophthalmic Surgeon</text>
    <text class="brand-quals" x="138" y="118" font-size="7.5">MBBS (Hons) MMed FRANZCO</text>
    <path d="M0,184 Q175,158 351,184 L351,200 L0,200 Z" fill="var(--brand-blue)"/>
    <path d="M0,182 Q175,156 351,182" fill="none" stroke="url(#silverCardA)" stroke-width="2.5"/>
    <text class="web" x="176" y="193" font-size="10" text-anchor="middle">bramwelkoske.com.au</text>
  </g>
</svg>

<!-- Practice manager business card -->
<svg class="card card--manager" viewBox="0 0 351 200" xmlns="http://www.w3.org/2000/svg">
  <defs><clipPath id="cardClipB"><rect width="351" height="200" rx="8"/></clipPath></defs>
  <g clip-path="url(#cardClipB)">
    <rect width="351" height="200" fill="var(--white)"/>
    <circle cx="54" cy="54" r="11" fill="var(--brand-blue)"/>
    <text class="brand-name" x="100" y="54" font-size="22">Dr Lars Brimwell</text>
    <text class="brand-role" x="101" y="66" font-size="8.5">Ophthalmic Surgeon</text>
    <text class="brand-quals" x="101" y="75" font-size="7">MBBS (Hons) MMed FRANZCO</text>

    <text x="20" y="116" font-family="Roboto, sans-serif" font-size="12" font-weight="500" fill="var(--brand-blue)">Fiona Pelkrest (BCom)</text>
    <text class="contact" x="20" y="129" font-size="8.8">Practice Manager for <tspan fill="var(--brand-blue)">Dr Lars Brimwell</tspan></text>
    <line x1="20" y1="138" x2="332" y2="138" stroke="var(--silver)" stroke-width="0.8"/>

    <circle cx="26" cy="151" r="4" fill="var(--brand-blue)"/>
    <text class="contact" x="35" y="154" font-size="8.8">(08) 9471 2630</text>
    <circle cx="26" cy="163" r="4" fill="var(--brand-blue)"/>
    <text class="contact" x="35" y="166" font-size="8.8">(08) 9471 2638</text>
    <circle cx="26" cy="175" r="4" fill="var(--brand-blue)"/>
    <text class="contact" x="35" y="178" font-size="8.8">reception@bramwelkoske.com.au</text>

    <text class="contact" x="332" y="152" font-size="8.8" text-anchor="end">24 Harrow Lane, Westmere</text>
    <text class="contact" x="332" y="165" font-size="8.8" text-anchor="end">Western Australia 6015</text>
    <text x="332" y="179" font-family="Roboto, sans-serif" font-size="8.8" text-anchor="end" fill="var(--brand-blue)">bramwelkoske.com.au</text>
  </g>
</svg>

<!-- USB drives -->
<svg class="usb usb--white" viewBox="0 0 130 52" xmlns="http://www.w3.org/2000/svg">
  <rect x="0" y="2" width="108" height="48" fill="var(--white)"/>
  <rect x="106" y="0" width="24" height="52" fill="var(--cap-dark)"/>
  <circle cx="54" cy="26" r="9" fill="var(--brand-blue)"/>
</svg>
<svg class="usb usb--blue" viewBox="0 0 130 52" xmlns="http://www.w3.org/2000/svg">
  <rect x="0" y="0" width="108" height="52" fill="var(--brand-blue)"/>
  <rect x="106" y="2" width="24" height="48" fill="#f2f2f2"/>
  <circle cx="54" cy="26" r="9" fill="var(--white)"/>
</svg>

</body>
</html>
```